K & D A/C Compressors' Business Card

Hello,

I need someone to create a new business card for my business. The name of my Business is: K & D A/C Compressors. I sell automotive air conditioning parts (a/c parts). I would like the business card to incorporate my logo, and to have an automotive feel to it. It is important that the business card feel like it is coming from an automotive parts business.

I already have a logo, which I will provide.

Thanks.
Updates

Project Deadline Extended Reason: I feel like extending the deadline until October 9, 2017, will allow for more time to design the business card. Thank you for your understanding. Added Monday, October 2, 2017

Target Market(s)

Consumers who need automotive a/c parts, and auto mechanics.

Industry/Entity Type

Automotive

Contact Information for Business Card

Business name: K & D A/C Compressors
Business Address: 48207 Southwest 36th Street, North Miami Beach, Florida 33162
Telephone: 305-472-1390
Fax: To be provided once I choose your design.
Website: www.kdcoolunits.example
Email: support@kdcoolunits.example
Names: To be provided once I choose your design.

Font styles to use
Sans Serif

Colors

Designer to choose colors to be used in the design.

Requirements
Must have
• The business card must include all of the "Business Card Details" and the logo I have uploaded.

```html
<!DOCTYPE html>
<html lang="en">
<head>
<meta charset="utf-8">
<title>K &amp; D A/C Compressors – Business Card</title>
<link rel="stylesheet" href="https://fonts.googleapis.com/css2?family=Open+Sans:wght@300;400;600;700&display=swap">
<style>
  :root {
    --backdrop: #3b3430;
    --card: #17181a;
    --card-edge: #222326;
    --accent: #29a9e1;
    --text-light: #f2f2f2;
    --text-muted: #9a9a9a;
    --divider: #8d8d8d;
  }
  * { box-sizing: border-box; margin: 0; padding: 0; }
  html, body {
    width: 1200px; height: 864px; overflow: hidden;
    background: var(--backdrop);
    font-family: "Open Sans", sans-serif;
  }
  .sheet {
    width: 1200px; height: 864px;
    display: flex; flex-direction: column;
    align-items: center; justify-content: center; gap: 56px;
  }
  .card {
    width: 620px; height: 354px;
    background: linear-gradient(160deg, var(--card-edge), var(--card) 60%);
    border-radius: 4px;
    box-shadow: 0 12px 30px rgba(0,0,0,.45);
    position: relative;
  }
  /* back side */
  .card-back {
    display: flex; flex-direction: column;
    align-items: center; justify-content: center; gap: 40px;
  }
  .back-name {
    font-size: 30px; font-weight: 600; color: var(--accent);
    letter-spacing: .5px;
  }
  .back-url {
    font-size: 13px; font-weight: 400; color: var(--text-muted);
    letter-spacing: 4px;
  }
  /* front side */
  .card-front { display: flex; align-items: center; }
  .brand {
    width: 290px; padding-left: 34px;
  }
  .brand-name {
    font-size: 27px; font-weight: 600; color: var(--text-light);
    line-height: 1.2;
  }
  .divider {
    width: 2px; height: 230px;
    background: linear-gradient(to bottom, transparent, var(--divider) 20%, var(--divider) 80%, transparent);
  }
  .contact { padding-left: 22px; color: var(--text-light); }
  .person-name {
    font-size: 19px; font-weight: 700; color: var(--accent);
    text-transform: uppercase; line-height: 1.1;
  }
  .person-role {
    font-size: 13px; font-weight: 400; color: var(--text-muted);
    margin-bottom: 6px;
  }
  .address { font-size: 14px; line-height: 1.35; margin-bottom: 6px; }
  .lines { list-style: none; font-size: 14px; line-height: 1.4; }
  .lines li { display: flex; align-items: center; gap: 9px; }
  .icon { width: 12px; height: 12px; flex: none; fill: var(--accent); }
</style>
</head>
<body>
<main class="sheet">
  <section class="card card-back" aria-label="Business card, back">
    <p class="back-name">K &amp; D A/C Compressors</p>
    <p class="back-url">www.kdcoolunits.example</p>
  </section>

  <section class="card card-front" aria-label="Business card, front">
    <div class="brand">
      <p class="brand-name">K &amp; D<br>A/C Compressors</p>
    </div>
    <div class="divider"></div>
    <div class="contact">
      <p class="person-name">Daniel Reyes</p>
      <p class="person-role">CEO/FOUNDER</p>
      <p class="address">48207 Southwest 36th Street<br>North Miami Beach, Florida 33162</p>
      <ul class="lines">
        <li><svg class="icon" viewBox="0 0 12 12"><path d="M2 1h3l1 3-1.5 1a7 7 0 0 0 2.5 2.5L8 6l3 1v3a1 1 0 0 1-1 1A9 9 0 0 1 1 2a1 1 0 0 1 1-1z"/></svg>305-472-1390</li>
        <li><svg class="icon" viewBox="0 0 12 12"><rect x="3" y="1" width="6" height="4"/><rect x="1" y="5" width="10" height="5" rx="1"/><rect x="3" y="8" width="6" height="3" fill="#17181a"/></svg>305-472-1391</li>
        <li><svg class="icon" viewBox="0 0 12 12"><rect x="1" y="2.5" width="10" height="7" rx="1"/><path d="M1.5 3l4.5 3.5L10.5 3" stroke="#17181a" stroke-width="1" fill="none"/></svg>support@kdcoolunits.example</li>
        <li><svg class="icon" viewBox="0 0 12 12"><circle cx="6" cy="6" r="5.5"/><path d="M6 3v3h2" stroke="#17181a" stroke-width="1.2" fill="none"/></svg>www.kdcoolunits.example</li>
      </ul>
    </div>
  </section>
</main>
</body>
</html>
```